Computer Company needs a Business card design

We need a business card design for our business. We assist people to transition to the QLX (Quorra Linkwave Exchange). The Australian Government-owned qlx™ network is a brand new telecommunications network currently being rolled out across Australia, giving access to a reliable broadband connection. Our niche market will predominantly be domestic customers in the 50+ age bracket. The assistance that we provide is everything from arranging the equipment, arranging the plan and contract term, appointment times, final testing of the network and any tweaks that need to be made. We basically PM the transition from start to finish. The business card design should be minimalist, should communicate loyalty and stability, should be easy to read and clearly explain what we do. We have asked for front and back. However, the back of the card does not have to include much information at all. It could be just a small design, or a repeat of our phone number. Up to you. The attached file only says what is required on the card. It does not specify where to arrange the text, what fonts to use, etc etc. As much as we would like to give you more info, due to our very limited design ability, we are not really able to send you any rough, or otherwise, designs of what we are after. Hopefully the above description is enough for you.

```html
<!DOCTYPE html>
<html lang="en">
<head>
<meta charset="utf-8">
<title>Tevra business card</title>
<link href="https://fonts.googleapis.com/css2?family=Quicksand:wght@300;400;500;600&display=swap" rel="stylesheet">
<style>
  :root {
    --page-bg: #f7f7f7;
    --front-bg: #333333;
    --back-bg: #1b1b1b;
    --card-edge: #2a2a2a;
    --brand-blue: #0d94db;
    --text-blue: #0ea0e2;
  }
  html, body {
    margin: 0;
    padding: 0;
    width: 1200px;
    height: 1200px;
    overflow: hidden;
    background: var(--page-bg);
    font-family: "Quicksand", sans-serif;
  }
  .canvas {
    position: relative;
    width: 1200px;
    height: 1200px;
  }
  .card {
    position: absolute;
    left: 171px;
    width: 858px;
    height: 477px;
    box-sizing: border-box;
    border: 1px solid var(--card-edge);
  }
  .card--front { top: 114px; background: var(--front-bg); }
  .card--back  { top: 609px; background: var(--back-bg); }

  .brand {
    position: absolute;
    color: var(--brand-blue);
    font-weight: 500;
    line-height: 1;
  }
  .brand__name {
    display: block;
    font-size: 66px;
    letter-spacing: 6px;
  }
  .brand__tagline {
    display: block;
    font-size: 27px;
    letter-spacing: 0.5px;
    margin-top: 4px;
  }
  .card--front .brand {
    left: 0;
    right: 0;
    top: 188px;
    text-align: center;
  }
  .card--back .brand {
    left: 80px;
    top: 30px;
  }

  .contact {
    position: absolute;
    right: 79px;
    top: 198px;
    text-align: right;
    color: var(--text-blue);
  }
  .contact__name {
    display: block;
    font-size: 50px;
    font-weight: 500;
    line-height: 1;
  }
  .contact__phone {
    display: block;
    font-size: 24px;
    font-weight: 300;
    margin-top: 8px;
    letter-spacing: 0.5px;
  }
  .website {
    position: absolute;
    left: 0;
    right: 0;
    top: 420px;
    text-align: center;
    color: var(--text-blue);
    font-size: 34px;
    font-weight: 300;
    line-height: 1;
  }
</style>
</head>
<body>
  <main class="canvas">
    <section class="card card--front" aria-label="Card front">
      <div class="brand">
        <span class="brand__name">Tevra</span>
        <span class="brand__tagline">qlx setup help</span>
      </div>
    </section>

    <section class="card card--back" aria-label="Card back">
      <div class="brand">
        <span class="brand__name">Tevra</span>
        <span class="brand__tagline">qlx setup help</span>
      </div>
      <div class="contact">
        <span class="contact__name">Owen Marlow</span>
        <span class="contact__phone">041 27 5 30 86</span>
      </div>
      <div class="website">www.tevrasetup.com.au</div>
    </section>
  </main>
</body>
</html>
```